Property inspection company needs logo/business card design

A new, home, commercial, and multi dwelling inspection company needs help with a new logo and hence business cards.

Time is extended for the rest of the week.

Font styles to use
Sans Serif

Colors
ec1f27
0255a3
ffffff

```html
<!DOCTYPE html>
<html lang="en">
<head>
<meta charset="utf-8">
<title>Carl Wendover Property Inspections – Business Cards</title>
<link rel="stylesheet" href="https://fonts.googleapis.com/css2?family=Oswald:wght@500;600&family=Open+Sans:wght@400;600;700&display=swap">
<style>
  :root {
    --stage: #dcdcdc;
    --stage-edge: #c9c9c9;
    --card-white: #ffffff;
    --brand-sky: #29a8ee;
    --brand-sky-deep: #1a8fe0;
    --brand-navy: #1b2a6b;
    --ink: #1e1e1e;
    --on-blue: #ffffff;
  }
  * { box-sizing: border-box; margin: 0; padding: 0; }
  html, body { width: 1200px; height: 900px; overflow: hidden; }
  body {
    background: radial-gradient(ellipse at 45% 40%, var(--stage) 0%, var(--stage-edge) 100%);
    position: relative;
    font-family: "Open Sans", sans-serif;
  }
  .card {
    position: absolute;
    width: 560px;
    height: 320px;
    border-radius: 28px;
    box-shadow: 0 10px 24px rgba(0,0,0,0.22);
    display: flex;
    flex-direction: column;
    align-items: center;
    justify-content: center;
    text-align: center;
  }
  .card-front {
    left: 60px; top: 100px;
    background: var(--card-white);
  }
  .card-back {
    left: 580px; top: 480px;
    background: linear-gradient(160deg, var(--brand-sky) 0%, var(--brand-sky-deep) 100%);
    color: var(--on-blue);
  }
  .brand-name {
    font-family: "Oswald", sans-serif;
    font-weight: 600;
    text-transform: uppercase;
    line-height: 1;
  }
  .card-front .brand-name { color: var(--brand-sky); }
  .brand-name .title { display: block; font-size: 44px; letter-spacing: 0.5px; }
  .brand-name .suffix { display: block; font-size: 15px; letter-spacing: 4px; margin-top: 6px; }
  .front-brand { display: flex; align-items: center; gap: 14px; margin-top: 10px; }
  .brand-dot { width: 18px; height: 18px; border-radius: 50%; background: var(--brand-sky); }
  .address { margin-top: 56px; font-size: 15px; color: var(--ink); letter-spacing: 0.3px; }

  .card-back .brand-name .title { font-size: 50px; }
  .card-back .brand-name .suffix { font-size: 16px; letter-spacing: 4.5px; }
  .rule { width: 290px; height: 1px; background: rgba(255,255,255,0.85); margin: 14px 0; }
  .person-name { font-weight: 700; font-size: 19px; letter-spacing: 1px; text-transform: uppercase; }
  .person-role { font-size: 13px; margin-top: 1px; }
  .contact-line { font-size: 13px; line-height: 1.55; }
  .contact-line b { font-weight: 700; }
</style>
</head>
<body>
  <section class="card card-front">
    <div class="front-brand">
      <span class="brand-dot"></span>
      <h1 class="brand-name">
        <span class="title">Carl Wendover</span>
        <span class="suffix">Property Inspections Inc</span>
      </h1>
    </div>
    <p class="address">4821, Harbor Ridge Lane Northfield, 604217.</p>
  </section>

  <section class="card card-back">
    <h2 class="brand-name">
      <span class="title">Carl Wendover</span>
      <span class="suffix">Property Inspections Inc</span>
    </h2>
    <div class="rule"></div>
    <p class="person-name">Daniel Price</p>
    <p class="person-role">Managing Director</p>
    <div class="rule"></div>
    <p class="contact-line"><b>P:</b> 055-210 384 617 | <b>M:</b> 055-210 384 617</p>
    <p class="contact-line"><b>E:</b> hello@wendoverinspect.com | <b>W:</b> www.wendoverinspect.com</p>
  </section>
</body>
</html>
```